owlbrass website

commerce website to sell cookeries, brackets, mailboxes and to show off homes built. Modern Steel in design see tandra wheels web page to be like: https://www.tandrawheels.example/en/ sorry its net haven hosting word press divi

must be able to add products to page

Target Market(s)

mainly western states of U.S.

Industry/Entity Type

Building Product

Coding

Coded - Design and coding required

Number of Pages Required

3 page

Font styles to use
Sans Serif

Colors

Designer to choose colors to be used in the design.

Requirements
Must have
• customers to be able to order products from page
• net haven hosting word press divi

```html
<!DOCTYPE html>
<html lang="en">
<head>
<meta charset="utf-8">
<title>Owl Brass — Home</title>
<link rel="stylesheet" href="https://fonts.googleapis.com/css2?family=Poppins:wght@400;500;600&family=Libre+Baskerville:wght@400;700&display=swap">
<style>
  :root {
    --navy: #4b5f8a;
    --navy-light: #5b6f99;
    --navy-dark: #3f5279;
    --orange: #ec5a2c;
    --ink: #2c2c2c;
    --paper: #ffffff;
    --mist: #f0f4f8;
    --sans: "Poppins", sans-serif;
    --serif: "Libre Baskerville", serif;
  }
  * { box-sizing: border-box; margin: 0; padding: 0; }
  html, body { width: 819px; height: 1200px; overflow: hidden; }
  body { position: relative; font-family: var(--sans); color: var(--ink); background: var(--paper); }
  .abs { position: absolute; }

  /* Header */
  .site-header { position: absolute; left: 0; top: 0; width: 819px; height: 97px; background: var(--paper); }
  .brand { position: absolute; left: 96px; top: 32px; display: flex; align-items: center; gap: 8px; }
  .brand-mark { width: 16px; height: 16px; background: var(--navy); }
  .brand-name { font-family: var(--sans); font-weight: 500; font-size: 21px; letter-spacing: 0.5px; color: var(--navy); }
  .contact-item { position: absolute; top: 16px; display: flex; gap: 5px; align-items: flex-start; }
  .contact-item svg { width: 18px; height: 18px; margin-top: 1px; }
  .contact-label { font-size: 7.5px; font-weight: 500; line-height: 10px; color: var(--ink); }
  .contact-value { font-size: 7.5px; line-height: 10px; color: var(--ink); }
  .main-nav { position: absolute; top: 62px; left: 0; width: 819px; }
  .main-nav a { position: absolute; font-size: 10px; color: var(--ink); text-decoration: none; }
  .main-nav a.is-active { font-weight: 500; }
  .main-nav a.is-active::after { content: ""; position: absolute; left: -2px; right: -3px; top: 16px; height: 1.5px; background: var(--orange); }

  /* Hero */
  .hero { position: absolute; left: 0; top: 97px; width: 819px; height: 361px;
    background: linear-gradient(180deg, #8fb0d4 0%, #b9cbe0 30%, #6d7a86 60%, #4a4e52 100%); }
  .hero-caption { position: absolute; left: 177px; top: 240px; width: 479px; height: 116px; background: rgba(40,40,44,0.55);
    display: flex; align-items: center; justify-content: center; }
  .hero-title { font-family: var(--serif); font-size: 23px; line-height: 29px; color: var(--paper); text-align: center; font-weight: 400; }

  /* Products */
  .products { position: absolute; left: 0; top: 458px; width: 819px; height: 437px; background: var(--mist); }
  .section-title { position: absolute; left: 0; width: 819px; text-align: center; font-family: var(--serif); font-weight: 700; font-size: 24px; color: var(--navy); }
  .rule { position: absolute; height: 1px; background: var(--orange); }
  .section-lead { position: absolute; left: 90px; top: 76px; width: 639px; text-align: center; font-size: 11px; line-height: 19.5px; color: #333; }
  .product-card { position: absolute; top: 128px; width: 198px; height: 231px; }
  .product-photo { position: absolute; left: 0; top: 0; width: 198px; height: 157px; }
  .product-info { position: absolute; left: 10px; top: 132px; width: 178px; height: 97px; background: var(--paper); text-align: center; box-shadow: 0 1px 3px rgba(0,0,0,0.06); }
  .product-name { margin-top: 14px; font-size: 14.5px; font-weight: 500; color: var(--orange); }
  .product-info .rule { left: 72px; width: 34px; top: 38px; }
  .product-text { margin-top: 16px; font-size: 9px; line-height: 15.5px; color: #333; }
  .shop-button { position: absolute; left: 366px; top: 376px; width: 87px; height: 24px; background: var(--orange); color: var(--paper);
    font-size: 9.5px; display: flex; align-items: center; justify-content: center; letter-spacing: 0.2px; }

  /* Goal band */
  .goal { position: absolute; left: 0; top: 895px; width: 819px; height: 155px; background: var(--navy); overflow: hidden; }
  .goal-skyline { position: absolute; left: 0; top: 40px; width: 819px; height: 115px;
    background: linear-gradient(180deg, rgba(63,82,121,0) 0%, rgba(63,82,121,0.7) 100%); }
  .goal-title { position: absolute; left: 0; width: 819px; text-align: center; font-family: var(--serif); font-weight: 700; color: var(--paper); }

  /* Footer */
  .footer-nav { position: absolute; left: 0; top: 1050px; width: 819px; height: 29px; background: var(--navy-light);
    border-top: 1px solid #6c7fa6; border-bottom: 1px solid #6c7fa6; }
  .footer-nav a { position: absolute; top: 8px; font-size: 10px; color: var(--paper); text-decoration: none; }
  .footer-nav a.is-active { font-weight: 600; }
  .footer-info { position: absolute; left: 0; top: 1079px; width: 819px; height: 91px; background: var(--navy); }
  .footer-brand { position: absolute; left: 136px; top: 37px; display: flex; align-items: center; gap: 6px; }
  .footer-brand .brand-mark { background: var(--paper); width: 12px; height: 12px; }
  .footer-brand .brand-name { color: var(--paper); font-size: 16px; }
  .divider { position: absolute; top: 23px; width: 1px; height: 38px; background: #6c7fa6; }
  .footer-contact { position: absolute; top: 33px; display: flex; gap: 5px; color: var(--paper); }
  .footer-contact svg { width: 18px; height: 18px; }
  .footer-contact .contact-label, .footer-contact .contact-value { color: var(--paper); }
  .social { position: absolute; top: 33px; width: 19px; height: 19px; border-radius: 50%; background: rgba(255,255,255,0.25); }
  .social.is-first { background: var(--paper); }
  .copyright { position: absolute; left: 0; top: 1170px; width: 819px; height: 30px; background: var(--orange);
    color: var(--paper); font-size: 9px; display: flex; align-items: center; justify-content: center; }
</style>
</head>
<body>

<header class="site-header">
  <div class="brand"><span class="brand-mark"></span><span class="brand-name">OWL BRASS</span></div>

  <div class="contact-item" style="left:512px;">
    <svg viewBox="0 0 18 18" fill="none" stroke="#ec5a2c" stroke-width="1"><rect x="1" y="4" width="16" height="11"/><path d="M1 4l8 7 8-7M1 15l6-5M17 15l-6-5"/></svg>
    <div><div class="contact-label">Email</div><div class="contact-value">inquiry@owlbrass.com</div></div>
  </div>
  <div class="contact-item" style="left:641px;">
    <svg viewBox="0 0 18 18" fill="none" stroke="#ec5a2c" stroke-width="1"><path d="M3 2l3 0 1.5 4-2 1.5c1 2.2 2.8 4 5 5l1.5-2 4 1.5v3c-7 .5-13.5-6-13-13z"/></svg>
    <div><div class="contact-label">Call Us</div><div class="contact-value">+ (123) 456 7890</div></div>
  </div>

  <nav class="main-nav">
    <a class="is-active" style="left:385px;">Home</a>
    <a style="left:443px;">Products</a>
    <a style="left:516px;">Home Built</a>
    <a style="left:597px;">About Us</a>
    <a style="left:669px;">Contact Us</a>
  </nav>
</header>

<section class="hero" role="img" aria-label="Photograph of a modern steel-clad home with large glass windows under trees and palms">
  <div class="hero-caption">
    <h1 class="hero-title">We Sell Cookeries, Brackets, Mailboxes<br>And To Show Off Homes Built</h1>
  </div>
</section>

<section class="products">
  <h2 class="section-title" style="top:34px;">Our Products</h2>
  <div class="rule" style="left:391px; width:38px; top:69px;"></div>
  <p class="section-lead">Lorem ipsum dolor sit amet, consectetuer adipiscing elit, sed diam nonummy nibh euismod tincidunt ut laoreet dolore magna aliquam erat volutpat Ut wisi enim ad minim.</p>

  <article class="product-card" style="left:96px;">
    <div class="product-photo" role="img" aria-label="Photograph of a dark steel-panelled entrance with sliding glass doors" style="background:linear-gradient(135deg,#3c4044 0%,#6b6f72 50%,#2e3134 100%);"></div>
    <div class="product-info">
      <h3 class="product-name">Steel Cookery</h3>
      <div class="rule"></div>
      <p class="product-text">Lorem ipsum dolor sit amet consec<br>tetuer adipiscing elit, sed diam</p>
    </div>
  </article>

  <article class="product-card" style="left:311px;">
    <div class="product-photo" role="img" aria-label="Photograph of a modern steel home with a bracket-framed glass facade" style="background:linear-gradient(180deg,#9fbad8 0%,#c4d2e0 40%,#6a7178 75%,#8a8a84 100%);"></div>
    <div class="product-info">
      <h3 class="product-name">Brackets</h3>
      <div class="rule"></div>
      <p class="product-text">Lorem ipsum dolor sit amet consec<br>tetuer adipiscing elit, sed diam</p>
    </div>
  </article>

  <article class="product-card" style="left:525px;">
    <div class="product-photo" role="img" aria-label="Photograph of a round steel fire-pit cooker in a workshop" style="background:linear-gradient(180deg,#8f8f8c 0%,#5d5e5e 45%,#242526 80%,#7a7976 100%);"></div>
    <div class="product-info">
      <h3 class="product-name">Mail Boxes</h3>
      <div class="rule"></div>
      <p class="product-text">Lorem ipsum dolor sit amet consec<br>tetuer adipiscing elit, sed diam</p>
    </div>
  </article>

  <a class="shop-button">SHOP NOW</a>
</section>

<section class="goal">
  <div class="goal-skyline" role="img" aria-label="Faint illustration of a city skyline"></div>
  <h2 class="goal-title" style="top:38px; font-size:32px;">Our Goal Is Simply To Build</h2>
  <p class="goal-title" style="top:84px; font-size:24px;">The Best Products In The World</p>
</section>

<nav class="footer-nav">
  <a class="is-active" style="left:242px;">Home</a>
  <a style="left:299px;">Products</a>
  <a style="left:371px;">Home Built</a>
  <a style="left:452px;">About Us</a>
  <a style="left:524px;">Contact Us</a>
</nav>

<footer class="footer-info">
  <div class="footer-brand"><span class="brand-mark"></span><span class="brand-name">OWL BRASS</span></div>
  <div class="divider" style="left:261px;"></div>
  <div class="footer-contact" style="left:295px;">
    <svg viewBox="0 0 18 18" fill="none" stroke="#ec5a2c" stroke-width="1"><rect x="1" y="4" width="16" height="11"/><path d="M1 4l8 7 8-7M1 15l6-5M17 15l-6-5"/></svg>
    <div><div class="contact-label">Email Us</div><div class="contact-value">inquiry@owlbrass.com</div></div>
  </div>
  <div class="divider" style="left:437px;"></div>
  <div class="footer-contact" style="left:471px; top:35px;">
    <svg viewBox="0 0 18 18" fill="none" stroke="#ec5a2c" stroke-width="1"><path d="M3 2l3 0 1.5 4-2 1.5c1 2.2 2.8 4 5 5l1.5-2 4 1.5v3c-7 .5-13.5-6-13-13z"/></svg>
    <div><div class="contact-label">Call Us On.</div><div class="contact-value">+ (123) 456 7890</div></div>
  </div>
  <div class="divider" style="left:586px;"></div>
  <span class="social is-first" style="left:621px;" aria-label="Social link"></span>
  <span class="social" style="left:644px;" aria-label="Social link"></span>
  <span class="social" style="left:667px;" aria-label="Social link"></span>
</footer>

<div class="copyright">Copyright © 2020 Owl Brass. All Rights Reserved.</div>

</body>
</html>
```